Logistics Website Design

See website https://tvarfreightglobal.com for theme and color details. Need the site to be re-done and reflect some of the designs shown in this list here: https://pinvora.com/tags/logistics-company-website

Target Market(s)

Logistics & Transportation

Industry/Entity Type

Logistics and Supply Chain

Coding

Coded - Design and coding required

Number of Pages Required

5+ page

Requirements
Must have
• Colors must match theme of logo. Looking for a sleek, interactive design.

```html
<!DOCTYPE html>
<html lang="en">
<head>
<meta charset="utf-8">
<title>Tvar Freight Global — Logistics</title>
<link href="https://fonts.googleapis.com/css2?family=Bebas+Neue&family=Poppins:wght@400;500;600&display=swap" rel="stylesheet">
<style>
:root{
  --orange:#e8602c;
  --brown:#4a190b;
  --brown-deep:#3a1207;
  --ink:#2b2b2b;
  --muted:#555;
  --white:#fff;
  --line:#cfcfcf;
}
*{box-sizing:border-box;margin:0;padding:0}
html,body{width:1200px;height:5204px;overflow:hidden}
body{font-family:"Poppins",sans-serif;color:var(--ink);background:#fff}
.page{position:relative;width:1200px;height:5204px;overflow:hidden}
.abs{position:absolute}
.display{font-family:"Bebas Neue",sans-serif;font-weight:400;letter-spacing:.5px}
.btn{position:absolute;display:flex;align-items:center;justify-content:center;color:#fff;font-weight:500;text-transform:uppercase;background:var(--orange);transform:skewX(-14deg);border-radius:6px}
.btn span{transform:skewX(14deg)}
.brand{position:absolute;display:flex;flex-direction:column;align-items:center;gap:8px}
.brand .mark{border-radius:50%;background:var(--orange)}
.brand .name{font-weight:600;font-size:17px;color:#fff;white-space:nowrap}

/* hero */
.hero{top:0;left:0;width:1200px;height:888px;background:linear-gradient(180deg,#2e3236 0%,#4a4d50 35%,#3a3a38 60%,#5a4a3c 80%,#6b5238 100%)}
.nav a{position:absolute;top:90px;font-size:13px;color:#fff;text-decoration:none}
.nav .active{color:var(--orange)}
.nav .active::after{content:"";position:absolute;left:0;right:0;bottom:-8px;height:2px;background:var(--orange)}
.nav-cta{top:78px;left:1020px;width:122px;height:42px;font-size:13px;text-transform:none}
.hero h1{left:66px;top:216px;font-size:132px;line-height:132px;color:#fff}
.hero p{left:70px;top:634px;width:420px;font-size:20px;line-height:38px;color:#fff}
.hero .btn{left:70px;top:746px;width:260px;height:64px;font-size:18px}

/* section titles */
.sec-title{position:absolute;left:0;width:1200px;text-align:center;font-size:62px;color:var(--brown)}
.rule{position:absolute;left:544px;width:112px;height:4px;background:var(--orange)}

/* services */
.card{position:absolute;width:444px;height:346px;border-radius:12px;overflow:hidden}
.card .ttl{position:absolute;left:28px;bottom:26px;font-size:34px;color:#fff}
.card svg{position:absolute;right:26px;bottom:32px}
.card::after{content:"";position:absolute;inset:0;background:linear-gradient(180deg,transparent 55%,rgba(0,0,0,.55));pointer-events:none}
.card .ttl,.card svg{z-index:2}

/* about */
.about{top:1978px;left:0;width:1200px;height:477px;background:var(--brown-deep)}
.about-photo{position:absolute;left:560px;top:0;width:640px;height:477px;clip-path:polygon(155px 0,640px 0,640px 477px,0 477px);background:linear-gradient(160deg,#3a4448 0%,#8d9499 40%,#d9dcde 55%,#5c5a4e 80%,#c9b24a 100%)}
.about h2{left:66px;top:70px;font-size:60px;color:#fff}
.about .rule{left:66px;top:146px;width:112px}
.about p{left:66px;top:184px;width:420px;font-size:13.5px;line-height:24px;color:#fff}
.about .btn{left:76px;top:376px;width:218px;height:58px;font-size:18px;text-transform:uppercase}

/* industries */
.ind{position:absolute;width:280px;height:137px;background:var(--orange);border-radius:8px;display:flex;align-items:flex-end;justify-content:center;padding-bottom:34px;text-align:center}
.ind .lbl{font-size:28px;line-height:28px;color:#fff}
.ind .badge{position:absolute;left:90px;top:-66px;width:100px;height:100px;border-radius:50%;background:var(--brown);border:6px solid #fff;display:flex;align-items:center;justify-content:center}

/* banner */
.banner{top:3358px;left:0;width:1200px;height:490px;background:linear-gradient(90deg,#c9cdcf 0%,#e6e7e6 30%,#aaa59c 55%,#e7e0d2 75%,#f3eee4 100%)}
.banner h2{left:720px;top:76px;width:420px;text-align:center;font-size:86px;line-height:80px;color:var(--brown)}
.banner .btn{left:774px;top:362px;width:290px;height:72px;font-size:22px;background:var(--brown);text-transform:uppercase}

/* contact */
.band{top:3848px;left:770px;width:200px;height:872px;background:var(--orange)}
.contact-photo{top:3985px;left:597px;width:535px;height:572px;border-radius:14px;background:linear-gradient(180deg,#6a86a0 0%,#c9a89a 40%,#e89a5e 55%,#4c4c50 75%,#2e2e30 100%)}
.contact h2{left:70px;top:3992px;font-size:62px;color:var(--brown)}
.contact .rule{left:72px;top:4064px;width:112px}
.contact h3{left:66px;top:4100px;font-size:28px;font-weight:500;color:var(--brown)}
.contact p{left:70px;top:4158px;font-size:17px;line-height:32px;color:var(--ink)}
.field{position:absolute;border:1.5px solid var(--line);border-radius:2px;font-size:12px;color:var(--muted);padding:16px 18px}
.contact .btn{left:80px;top:4484px;width:186px;height:72px;font-size:24px}

/* footer */
.footer{top:4720px;left:0;width:1200px;height:484px;background:var(--brown-deep)}
.footer h4{position:absolute;top:120px;font-size:23px;font-weight:500;color:#fff}
.footer ul{position:absolute;left:292px;top:196px;list-style:none}
.footer li{font-size:13.5px;color:#fff;height:32.5px}
.footer li::before{content:"»";margin-right:12px}
.contact-row{position:absolute;left:808px;display:flex;align-items:center;gap:16px;color:#fff;font-size:13.5px;line-height:22px}
.contact-row .ic{width:38px;height:38px;border-radius:50%;background:#fff;display:flex;align-items:center;justify-content:center;flex:none}
.social{position:absolute;top:294px;width:36px;height:36px;border-radius:50%;background:var(--orange)}
.footer .hr{position:absolute;left:70px;top:388px;width:1060px;height:1px;background:rgba(255,255,255,.18)}
.footer .copy{position:absolute;left:0;top:422px;width:1200px;text-align:center;font-size:13.5px;color:#fff}
</style>
</head>
<body>
<div class="page">

  <!-- HERO -->
  <section class="abs hero" role="img" aria-label="Convoy of trucks driving on a highway at dusk under a cloudy sky">
  </section>
  <nav class="nav">
    <a class="active" style="left:130px">Home</a>
    <a style="left:225px">Services ▾</a>
    <a style="left:337px">Industries ▾</a>
    <a style="left:748px">Request A Quote</a>
    <a style="left:922px">About Us</a>
  </nav>
  <div class="btn nav-cta"><span>Contact Us</span></div>
  <div class="brand" style="left:500px;top:40px;width:200px">
    <div class="mark" style="width:62px;height:62px"></div>
    <div class="name">Tvar Freight Global</div>
  </div>
  <div class="hero">
    <h1 class="abs display">Delivering<br>Strength in<br>Every Mile</h1>
    <p class="abs">Secure and reliable transportation for all your cargo needs.</p>
    <div class="btn"><span>Request a Quote</span></div>
  </div>

  <!-- SERVICES -->
  <h2 class="sec-title display" style="top:964px">Our Services</h2>
  <div class="rule" style="top:1048px"></div>

  <div class="card" style="left:134px;top:1122px;background:linear-gradient(180deg,#8ea7c0 0%,#d6d9d6 45%,#c99a2e 65%,#5f6b3a 100%)" role="img" aria-label="Yellow flatbed truck on an open road">
    <div class="ttl display">Flatbed Transportation</div>
    <svg width="28" height="28" viewBox="0 0 28 28"><circle cx="14" cy="14" r="12" fill="none" stroke="#fff" stroke-width="2"/><path d="M10 18 L18 10 M12 10 H18 V16" fill="none" stroke="#fff" stroke-width="2"/></svg>
  </div>
  <div class="card" style="left:622px;top:1122px;background:linear-gradient(180deg,#9aa4b4 0%,#cfcfd4 35%,#3a4a66 65%,#2a2e38 100%)" role="img" aria-label="Fleet of step deck trucks parked under a cloudy sky">
    <div class="ttl display">Step Deck Transportation</div>
    <svg width="28" height="28" viewBox="0 0 28 28"><circle cx="14" cy="14" r="12" fill="none" stroke="#fff" stroke-width="2"/><path d="M10 18 L18 10 M12 10 H18 V16" fill="none" stroke="#fff" stroke-width="2"/></svg>
  </div>
  <div class="card" style="left:134px;top:1508px;background:linear-gradient(110deg,#5b8a2a 0%,#8fa66a 35%,#b8a89a 55%,#6f9a36 100%)" role="img" aria-label="Aerial view of a dry van truck on a country road">
    <div class="ttl display">Dry Van Transportation</div>
    <svg width="28" height="28" viewBox="0 0 28 28"><circle cx="14" cy="14" r="12" fill="none" stroke="#fff" stroke-width="2"/><path d="M10 18 L18 10 M12 10 H18 V16" fill="none" stroke="#fff" stroke-width="2"/></svg>
  </div>
  <div class="card" style="left:622px;top:1508px;background:linear-gradient(180deg,#8fb4dc 0%,#b8cfe6 40%,#4a5260 65%,#2a3f7a 100%)" role="img" aria-label="Heavy haul truck carrying oversized load">
    <div class="ttl display">Heavy Haul Transportation</div>
    <svg width="28" height="28" viewBox="0 0 28 28"><circle cx="14" cy="14" r="12" fill="none" stroke="#fff" stroke-width="2"/><path d="M10 18 L18 10 M12 10 H18 V16" fill="none" stroke="#fff" stroke-width="2"/></svg>
  </div>

  <!-- ABOUT -->
  <section class="abs about">
    <div class="about-photo" role="img" aria-label="Row of white box trucks parked at a loading dock"></div>
    <h2 class="abs display">About Us</h2>
    <div class="rule"></div>
    <p class="abs">We deliver a comprehensive range of open-deck and specialized transportation services—including flatbed, step deck, heavy haul, and over-dimensional freight solutions. Backed by years of experience, a trusted nationwide carrier network, and a strong safety-first culture, we provide reliable, adaptable logistics support built around the unique requirements of every load.</p>
    <div class="btn"><span>Know More</span></div>
  </section>

  <!-- INDUSTRIES -->
  <h2 class="sec-title display" style="top:2592px">Industries We Served</h2>
  <div class="rule" style="top:2676px"></div>

  <div class="ind" style="left:99px;top:2822px">
    <div class="badge"><svg width="48" height="48" viewBox="0 0 48 48" fill="none" stroke="#fff" stroke-width="2.4" stroke-linejoin="round"><rect x="10" y="20" width="28" height="20" rx="2"/><path d="M10 27h28M17 20v-6h14v6M21 14v-5h6v5"/><path d="M16 33h6M26 33h6"/></svg></div>
    <div class="lbl display">Food &amp; Beverage</div>
  </div>
  <div class="ind" style="left:456px;top:2822px">
    <div class="badge"><svg width="48" height="48" viewBox="0 0 48 48" fill="none" stroke="#fff" stroke-width="2.4" stroke-linejoin="round"><path d="M8 18l4-9h24l4 9z"/><path d="M8 18c0 3 3 5 5.5 5S19 21 19 18c0 3 2.5 5 5 5s5-2 5-5c0 3 3 5 5.5 5S40 21 40 18"/><path d="M11 23v17h26V23"/><rect x="18" y="29" width="12" height="11"/></svg></div>
    <div class="lbl display">E-Commerce &amp; Retail</div>
  </div>
  <div class="ind" style="left:821px;top:2822px">
    <div class="badge"><svg width="48" height="48" viewBox="0 0 48 48" fill="none" stroke="#fff" stroke-width="2.4" stroke-linejoin="round"><path d="M7 40V22l10 6v-6l10 6v-6l10 6V8h5v32z"/><path d="M13 34h4M22 34h4M31 34h4"/></svg></div>
    <div class="lbl display">Manufacturing</div>
  </div>
  <div class="ind" style="left:274px;top:3067px">
    <div class="badge"><svg width="48" height="48" viewBox="0 0 48 48" fill="none" stroke="#fff" stroke-width="2.4" stroke-linejoin="round"><rect x="9" y="9" width="30" height="30" rx="4"/><path d="M24 16v16M16 24h16"/></svg></div>
    <div class="lbl display">Pharma &amp; Healthcare</div>
  </div>
  <div class="ind" style="left:639px;top:3067px;padding-bottom:18px">
    <div class="badge"><svg width="50" height="48" viewBox="0 0 50 48" fill="none" stroke="#fff" stroke-width="2.4" stroke-linejoin="round"><path d="M4 34V14h26v20M30 20h8l7 7v7h-15"/><circle cx="13" cy="36" r="4"/><circle cx="37" cy="36" r="4"/><path d="M17 18l-6 11h12z"/><path d="M17 22v3"/></svg></div>
    <div class="lbl display">Government Secured<br>Freight</div>
  </div>

  <!-- BANNER -->
  <section class="abs banner" role="img" aria-label="White semi truck speeding along a highway with motion blur">
    <h2 class="abs display">Keeping Your Supply Chain Moving</h2>
    <div class="btn"><span>Request a Quote</span></div>
  </section>

  <!-- CONTACT -->
  <div class="abs band"></div>
  <div class="abs contact-photo" role="img" aria-label="Red semi truck driving on a highway at sunset"></div>
  <section class="contact">
    <h2 class="abs display">Contact Us</h2>
    <div class="rule"></div>
    <h3 class="abs">Let's Move Your Business Forward</h3>
    <p class="abs">Let's discuss your logistics needs and<br>how we can help your business thrive</p>
    <div class="field" style="left:66px;top:4266px;width:236px;height:42px;padding-top:12px">Your Name</div>
    <div class="field" style="left:312px;top:4266px;width:236px;height:42px;padding-top:12px">Phone Number</div>
    <div class="field" style="left:66px;top:4320px;width:482px;height:42px;padding-top:12px">Email Address</div>
    <div class="field" style="left:66px;top:4374px;width:482px;height:80px">Message</div>
    <div class="btn"><span>Submit</span></div>
  </section>

  <!-- FOOTER -->
  <footer class="abs footer">
    <h4 style="left:290px">LINKS</h4>
    <ul>
      <li>About Us</li><li>Properties</li><li>Services</li><li>Testimonials</li><li>Contact</li>
    </ul>
    <div class="brand" style="left:490px;top:110px;width:220px">
      <div class="mark" style="width:70px;height:70px"></div>
      <div class="name">Tvar Freight Global</div>
    </div>
    <div class="social" style="left:534px"></div>
    <div class="social" style="left:582px"></div>
    <div class="social" style="left:630px"></div>

    <h4 style="left:808px">CONTACT US</h4>
    <div class="contact-row" style="top:186px">
      <div class="ic"><svg width="16" height="20" viewBox="0 0 16 20"><path d="M8 1C4 1 1 4 1 8c0 5 7 11 7 11s7-6 7-11c0-4-3-7-7-7z" fill="#3a1207"/><circle cx="8" cy="8" r="2.5" fill="#fff"/></svg></div>
      <div>48 Harbor Freight Way,<br>Dayton OH 45402</div>
    </div>
    <div class="contact-row" style="top:246px">
      <div class="ic"><svg width="18" height="18" viewBox="0 0 18 18"><path d="M4 1l3 4-2 2c1 2 3 4 5 5l2-2 4 3-2 3C8 16 2 10 1 4z" fill="#3a1207"/></svg></div>
      <div>(555) 014 2276</div>
    </div>
    <div class="contact-row" style="top:300px">
      <div class="ic"><svg width="18" height="14" viewBox="0 0 18 14"><rect x="1" y="1" width="16" height="12" rx="1" fill="#3a1207"/><path d="M1 2l8 6 8-6" fill="none" stroke="#fff" stroke-width="1.4"/></svg></div>
      <div>hello@tvarfreight.com</div>
    </div>
    <div class="hr"></div>
    <div class="copy">Copyright © 2026 All Rights Reserved By Tvar Freight Global</div>
  </footer>

</div>
</body>
</html>
```